Brelvo Pizza & Pasta Takeaway Flyer

Our takeaway shop needs a well designed flyer for print and letter box distribution. Design to have a clear list of menu, Specials, contact details. If menu doesn't fit into A4, we won't mind going upto extended A4. I have attached draft copy of our menu and list of item in excel. Please add 5mm Bleed to the flyer.
Flyer will get printed on 115gsm Gloss stock.

```html
<!DOCTYPE html>
<html lang="en">
<head>
<meta charset="utf-8">
<title>Brelvo Pizza &amp; Pasta – Takeaway Menu</title>
<link href="https://fonts.googleapis.com/css2?family=Kaushan+Script&family=Open+Sans:ital,wght@0,400;0,600;1,400&display=swap" rel="stylesheet">
<style>
:root{
  --panel-dark:#222222;
  --panel-mid:#333333;
  --leaf:#9ccb45;
  --leaf-deep:#5f9a22;
  --item-green:#8dc63f;
  --price-red:#b52e2c;
  --brand-red:#b3272c;
  --brand-red-deep:#8e1d22;
  --ink:#3a3a3a;
  --light:#e6e6e6;
  --crust:#b86a3e;
  --cheese:#f1e4d2;
}
*{box-sizing:border-box;margin:0;padding:0}
html,body{width:1200px;height:848px;overflow:hidden;background:#fff}
body{font-family:"Open Sans",Arial,sans-serif;position:relative}
.menu{position:relative;width:1200px;height:848px;overflow:hidden}

.panel-dark{position:absolute;top:0;height:848px;background:radial-gradient(ellipse at 50% 40%,var(--panel-mid),var(--panel-dark) 75%)}
.panel-left{left:0;width:298px}
.panel-right{left:892px;width:308px}
.pizza-photo{position:absolute;left:298px;top:0;width:594px;height:848px;
  background:
    radial-gradient(ellipse 60% 12% at 50% 0%,rgba(120,50,25,.75),rgba(120,50,25,0) 100%),
    radial-gradient(ellipse 70% 55% at 50% 45%,rgba(250,244,236,.95),rgba(250,244,236,0) 80%),
    radial-gradient(ellipse 50% 30% at 20% 95%,rgba(190,120,80,.55),rgba(190,120,80,0) 100%),
    radial-gradient(ellipse 50% 30% at 85% 92%,rgba(190,120,80,.5),rgba(190,120,80,0) 100%),
    linear-gradient(180deg,var(--crust) 0%,#dcae88 12%,var(--cheese) 26%,#f3ebe2 55%,#e8d3bd 82%,#d3a883 100%)}

.section-bar{position:absolute;height:31px;display:flex;align-items:center;
  background:linear-gradient(180deg,#b6dc62 0%,var(--leaf) 45%,var(--leaf-deep) 100%);
  border-bottom:2px solid #fff;color:#fff}
.section-bar h2{font-family:"Kaushan Script",cursive;font-weight:400;font-size:21px;letter-spacing:.5px;text-shadow:0 1px 2px rgba(0,0,0,.35)}
.section-bar .sub{font-style:italic;font-size:11px;margin-left:8px}

.list{position:absolute;list-style:none}
.item{margin-bottom:9.6px}
.item.has-desc{margin-bottom:4px}
.row{display:flex;align-items:baseline;line-height:16px;font-size:13px;color:var(--item-green)}
.row .size{font-style:italic;font-size:10px;margin-left:3px}
.row .dots{flex:1;border-bottom:2px dotted #bbb;margin:0 5px;transform:translateY(-3px)}
.row .price{color:var(--price-red);font-size:13px}
.desc{font-style:italic;font-size:9.6px;line-height:14.4px;color:var(--light);padding-left:24px}
.note{position:absolute;font-style:italic;font-size:9.6px;color:var(--light)}

.list.mains .item.has-desc{margin-bottom:1px}
.list.mains .desc{line-height:13.6px;padding-left:26px}

.list.pasta .item{margin-bottom:0}
.list.pasta .row{line-height:14.4px}
.list.pasta .desc{padding-left:23px}

.list.subs .item{margin-bottom:3.2px}
.list.subs .row{line-height:19.2px}
.list.subs .desc{padding-left:22px}

.pizza-title{position:absolute;left:298px;width:594px;top:0;text-align:center;
  font-family:"Kaushan Script",cursive;font-weight:400;font-size:56px;color:var(--brand-red);
  text-shadow:0 0 8px rgba(255,255,255,.7)}
.pizza-note{position:absolute;font-style:italic;font-size:9.4px;color:var(--brand-red);line-height:13.6px}

.price-box{position:absolute;height:57px;width:277px;border-radius:4px;
  background:linear-gradient(180deg,#c0302f,var(--brand-red) 60%,var(--brand-red-deep));color:#fff;
  box-shadow:0 1px 3px rgba(0,0,0,.3)}
.price-box .range{position:absolute;left:14px;top:11px;font-family:"Kaushan Script",cursive;font-size:25px}
.price-box .col{position:absolute;top:8px;width:60px;margin-left:-30px;text-align:center}
.price-box .col span{display:block;font-size:10.5px;letter-spacing:.3px}
.price-box .col b{display:block;font-family:"Kaushan Script",cursive;font-weight:400;font-size:19px;margin-top:3px}
.calzone-bar{position:absolute;left:604px;top:705px;width:277px;height:33px;border-radius:3px;
  background:linear-gradient(180deg,#c0302f,var(--brand-red-deep));color:#fff}
.calzone-bar h3{font-family:"Kaushan Script",cursive;font-weight:400;font-size:20px;margin:3px 0 0 16px}

.pizzas{position:absolute;list-style:none}
.pizzas .item{margin-bottom:0}
.pizzas .item.solo{margin-bottom:4.8px}
.pizzas .name{font-size:13px;line-height:16px;color:var(--brand-red)}
.pizzas .desc{color:var(--ink);font-size:9.4px;line-height:13.6px;padding-left:20px}
.pizzas.tight .item{margin-bottom:3.6px}
.pizzas.tight .item.lead{margin-bottom:-1.6px}
.pizzas.tight .name{line-height:12px}
.pizzas .row{color:var(--brand-red)}
.pizzas .row .dots{border-bottom-color:#666}
.pizzas.calzones .desc{padding-left:20px}
.pizzas.calzones .item{margin-bottom:6px}

.seal{position:absolute;left:1090px;top:726px;width:96px;height:96px}
.seal-price{position:absolute;left:1088px;top:755px;width:100px;text-align:center;
  font-family:"Kaushan Script",cursive;font-size:31px;color:#fff}
</style>
</head>
<body>
<main class="menu">
  <div class="panel-dark panel-left"></div>
  <div class="pizza-photo" role="img" aria-label="Faded photograph of a loaded pizza with mushrooms, olives and capsicum behind the pizza list"></div>
  <div class="panel-dark panel-right"></div>

  <header class="section-bar" style="left:0;top:0;width:298px;padding-left:44px"><h2>Starters</h2></header>
  <ul class="list" style="left:14px;top:53px;width:268px">
    <li class="item"><div class="row">Garlic Bread<span class="dots"></span><span class="price">$3.95</span></div></li>
    <li class="item"><div class="row">Cheesy Garlic Bread<span class="dots"></span><span class="price">$5.50</span></div></li>
    <li class="item has-desc"><div class="row">Sweet Chilli Cheese Pizza<span class="dots"></span><span class="price">$7.95</span></div>
      <p class="desc">Sweet Chilli Sauce Base topped<br>with Cheese &amp; Herbs</p></li>
    <li class="item has-desc"><div class="row">Chips<span class="size">(Lge+$2)</span><span class="dots"></span><span class="price">$4.95</span></div>
      <p class="desc">with tomato sauce</p></li>
    <li class="item"><div class="row">Chips &amp; Gravy<span class="dots"></span><span class="price">$6.95</span></div></li>
    <li class="item"><div class="row">Beer Battered Chips<span class="dots"></span><span class="price">$6.95</span></div></li>
    <li class="item has-desc"><div class="row">Curly Fries<span class="size">(Lge+$2.5)</span><span class="dots"></span><span class="price">$5.95</span></div>
      <p class="desc">with Ranch Dip</p></li>
    <li class="item has-desc"><div class="row">Sweet Potato Chips<span class="dots"></span><span class="price">$6.95</span></div>
      <p class="desc">with Garlic Aioli Sauce</p></li>
    <li class="item has-desc"><div class="row">Onion Rings<span class="dots"></span><span class="price">$6.50</span></div>
      <p class="desc">with Ranch Dip</p></li>
    <li class="item has-desc"><div class="row">Chicken Nuggets(8Pcs)<span class="dots"></span><span class="price">$4.95</span></div>
      <p class="desc">with tomato sauce</p></li>
    <li class="item has-desc"><div class="row">Pepper Squid</div>
      <p class="desc">with Lemon Wedge</p></li>
    <li class="item has-desc"><div class="row">Chicken Chilli<span class="dots"></span><span class="price">$7.95</span></div>
      <p class="desc">with Lemon Wedge</p></li>
  </ul>
  <p class="note" style="left:16px;top:458px">**Add Extra Sauce $0.75</p>

  <header class="section-bar" style="left:0;top:496px;width:298px;padding-left:34px"><h2>Main</h2><span class="sub">[Served with Chips &amp; Garden Salad]</span></header>
  <ul class="list mains" style="left:14px;top:547px;width:274px">
    <li class="item"><div class="row">Chicken Schnitzel with Gravy<span class="dots"></span><span class="price">$16.00</span></div></li>
    <li class="item"><div class="row">Veal Schnitzel with Gravy<span class="dots"></span><span class="price">$16.00</span></div></li>
    <li class="item"><div class="row">Chicken Parmigiana<span class="dots"></span><span class="price">$17.00</span></div></li>
    <li class="item has-desc"><div class="row">Three Cheese Parmigiana<span class="dots"></span><span class="price">$17.00</span></div>
      <p class="desc">Topped with Parmesan, Mozzarella,<br>Bocconcini &amp; Herbs</p></li>
    <li class="item has-desc" style="margin-bottom:5px"><div class="row">Hawaiian Parmigiana<span class="dots"></span><span class="price">$17.00</span></div>
      <p class="desc">Topped with Cheese, Ham, Pineapple &amp; Herbs</p></li>
    <li class="item has-desc"><div class="row">Mexican Parmigiana<span class="dots"></span><span class="price">$17.00</span></div>
      <p class="desc">Topped with Cheese, Roasted Capsicum,<br>Jalapenos &amp; Herbs</p></li>
    <li class="item has-desc" style="margin-bottom:5px"><div class="row">Marinara Parmigiana<span class="dots"></span><span class="price">$19.00</span></div>
      <p class="desc">Topped with Cheese, Seafood mix &amp; Herbs</p></li>
    <li class="item has-desc"><div class="row">Creamy Garlic Prawn<span class="dots"></span><span class="price">$19.00</span></div>
      <p class="desc">Tiger Prawn, Garlic, White Wine, Spices<br>&amp; Herbs Pan fried with Creamy sauce</p></li>
  </ul>

  <h1 class="pizza-title">Pizza</h1>
  <p class="pizza-note" style="left:322px;top:68px">** Thin Base Available **<br>** GF base avilable only in large size. Extra $3 **</p>
  <p class="pizza-note" style="left:616px;top:82px">** Each Extra Topping - Small $1, Large $2, Family $3 **</p>

  <div class="price-box" style="left:308px;top:100px">
    <span class="range">Lite</span>
    <div class="col" style="left:107px"><span>SMALL</span><b>$9</b></div>
    <div class="col" style="left:170px"><span>LARGE</span><b>$13</b></div>
    <div class="col" style="left:232px"><span>FAMILY</span><b>$20</b></div>
  </div>
  <ul class="pizzas" style="left:326px;top:166px;width:262px">
    <li class="item solo"><p class="name">Hawaiian</p><p class="desc">Cheese, Ham &amp; Pineapple</p></li>
    <li class="item solo"><p class="name">Margherita</p><p class="desc">Cheese, Tomatoes, Basil &amp; Oregano</p></li>
    <li class="item solo"><p class="name">Mozzy</p><p class="desc">Cheese</p></li>
    <li class="item solo"><p class="name">NewYorker</p><p class="desc">Pepperoni, Basil &amp; Oregano</p></li>
    <li class="item"><p class="name">Veggie</p><p class="desc">Onion, Tomato, Mushroom, Capsicum, Olives,<br>Pineapple, Basil &amp; Oregano</p></li>
  </ul>

  <div class="price-box" style="left:308px;top:361px">
    <span class="range">Classic</span>
    <div class="col" style="left:115px"><span>SMALL</span><b>$11</b></div>
    <div class="col" style="left:173px"><span>LARGE</span><b>$15</b></div>
    <div class="col" style="left:233px"><span>FAMILY</span><b>$22</b></div>
  </div>
  <ul class="pizzas" style="left:326px;top:428px;width:268px">
    <li class="item"><p class="name">Supreme</p><p class="desc">Cheese, Pepperoni, Ham, Beef, Onion, Olives,<br>Capsicum, Pineapple &amp; Mushroom</p></li>
    <li class="item"><p class="name">Meat Lovers</p><p class="desc">Cheese, Pepperoni, Salami, Ham, Bacon, Chorizo<br>&amp; BBQ Sauce</p></li>
    <li class="item solo"><p class="name">Ozzy</p><p class="desc">Cheese, Chorizo, Bacon, Onion &amp; Egg</p></li>
    <li class="item solo"><p class="name">BBQ Chicken</p><p class="desc">Cheese, Chicken, Bacon, Mushroom &amp; BBQ Sauce</p></li>
    <li class="item solo"><p class="name">Tropical Chicken</p><p class="desc">Cheese, Chicken, Ham, Pineapple</p></li>
    <li class="item solo"><p class="name">Outback</p><p class="desc">Cheese, Ham, Salami, Bacon, Mushroom &amp; Onion</p></li>
    <li class="item solo"><p class="name">Spicy Pizza</p><p class="desc">Cheese, Pepperoni, Onion, Jalapenos &amp; Chilli Flakes</p></li>
    <li class="item"><p class="name">Mexican</p><p class="desc">Cheese, Beef, Pepperoni, Onion, Roasted Capsicum,<br>Jalapenos, Chilli &amp; Sourcream</p></li>
    <li class="item solo"><p class="name">Capricciosa</p><p class="desc">Cheese, Ham, Salami, Mushroom, Tomato &amp; Olives</p></li>
    <li class="item"><p class="name">Veg Supreme</p><p class="desc">Cheese, Tomato, Onion, Mushroon, Roasted<br>Capsicum, Pineapple, Fetta, Jalapenos &amp; Chilli</p></li>
    <li class="item"><p class="name">Four Cheese</p><p class="desc">Cheese, Fetta, Bocconcini, Parmesan &amp; Basil</p></li>
  </ul>

  <div class="price-box" style="left:604px;top:100px">
    <span class="range">Premium</span>
    <div class="col" style="left:126px"><span>SMALL</span><b>$13</b></div>
    <div class="col" style="left:183px"><span>LARGE</span><b>$19</b></div>
    <div class="col" style="left:243px"><span>FAMILY</span><b>$25</b></div>
  </div>
  <ul class="pizzas tight" style="left:622px;top:167px;width:262px">
    <li class="item lead"><p class="name">Garden Gourmet</p><p class="desc">Cheese, Semi-dried tomato, Mushrooms, Onion,<br>Roasted Capsicum, Olives, Cherry Tomato, Spinach,<br>Bocconcini &amp; Basil</p></li>
    <li class="item"><p class="name">Paneer Tikka</p><p class="desc">Cheese, Marinated Paneer, Onion, Tomato,<br>Capsicum, Olives &amp; Corinander</p></li>
    <li class="item"><p class="name">Pesto Chicken</p><p class="desc">Cheese, Chicken, Sun-Dried Tomato, Onion, Fetta<br>&amp; Parsley</p></li>
    <li class="item"><p class="name">Butter Chicken</p><p class="desc">Cheese, Marinated Chicken, Onion, Capsicum,<br>Corinader, Cashew &amp; Lemon Wedge</p></li>
    <li class="item"><p class="name">Meat &amp; Chicken</p><p class="desc">Pulled Beef, Pepperoni, Chicken, Salami, Roasted<br>Capsicum, Onion, Mushroom, Onion &amp; BBQ Sauce</p></li>
    <li class="item"><p class="name">Mediterranean</p><p class="desc">Pepperoni, Roasted Capsicum, Mushroom, Chorizo,<br>Olives, Fetta &amp; Bocconcini</p></li>
    <li class="item"><p class="name">The Lot</p><p class="desc">Ham, Pepperoni, Salami, Pulled Beef, Sausage,<br>Capsicum, Onion, Olives, Tomato, Pineapple,<br>Basil &amp; Oregano</p></li>
  </ul>

  <div class="price-box" style="left:604px;top:498px">
    <span class="range">Seafood</span>
    <div class="col" style="left:118px"><span>SMALL</span><b>$14</b></div>
    <div class="col" style="left:180px"><span>LARGE</span><b>$21</b></div>
    <div class="col" style="left:242px"><span>FAMILY</span><b>$28</b></div>
  </div>
  <ul class="pizzas tight" style="left:622px;top:567px;width:262px">
    <li class="item"><p class="name">The Pacific</p><p class="desc">Seafood Mix, Mushrooms, Roasted Capsicum &amp;<br>Garlic Oil (AnchoviesSuggested)</p></li>
    <li class="item"><p class="name">Reef n Turf</p><p class="desc">Prawn, PulledBeef, Onion, Mushroom, Capsicum,<br>Olives &amp; Garlic Sauce</p></li>
    <li class="item"><p class="name">Prawn &amp; Garlic</p><p class="desc">Prawns, Cheery Tomato, Spinach, Bocconcini &amp;<br>Garlic Sauce</p></li>
  </ul>

  <div class="calzone-bar"><h3>Calzone</h3></div>
  <ul class="pizzas calzones" style="left:622px;top:749px;width:240px">
    <li class="item"><div class="row">Classic Calzone<span class="dots"></span><span class="price">$16</span></div><p class="desc">Folded Pizza, Rolled &amp; Cooked, Sealing<br>in all Flaours from Classic Pizza range.</p></li>
    <li class="item"><div class="row">Premium Calzone<span class="dots"></span><span class="price">$18</span></div><p class="desc">Folded Pizza, Rolled &amp; Cooked, Sealing<br>in all Flaours from Premium Pizza range.</p></li>
  </ul>

  <header class="section-bar" style="left:892px;top:0;width:308px;padding-left:46px"><h2>Pasta</h2></header>
  <ul class="list pasta" style="left:907px;top:52px;width:275px">
    <li class="item"><div class="row">Napoletana<span class="dots"></span><span class="price">$14.00</span></div><p class="desc">Tomatoes, Onions, and Special Italian<br>Herbs in Red Pasta sauce</p></li>
    <li class="item"><div class="row">Vegetaria<span class="dots"></span><span class="price">$16.00</span></div><p class="desc">Mushroom, Tomatoes, Onions,Capsicum<br>and Special Italian Herbs in Red Pasta sauce</p></li>
    <li class="item"><div class="row">Bolognese<span class="dots"></span><span class="price">$16.00</span></div><p class="desc">Traditional Beef, Onions and Special Italian<br>Herbs in Red Pasta sauce</p></li>
    <li class="item"><div class="row">Carbonara<span class="dots"></span><span class="price">$16.00</span></div><p class="desc">Bacon, Eggs &amp; Mushrooms in a Creamy<br>White Sauce</p></li>
    <li class="item"><div class="row">Alla Panna<span class="dots"></span><span class="price">$16.00</span></div><p class="desc">Ham &amp; Mushrooms in a Creamy White Sauce</p></li>
    <li class="item" style="padding-top:6px"><div class="row">Chicken Carbonara<span class="dots"></span><span class="price">$16.00</span></div><p class="desc">Chicken, Eggs, Mushrooms &amp; Onions in a<br>Creamy White Sauce</p></li>
    <li class="item"><div class="row">Chicken<span class="dots"></span><span class="price">$16.00</span></div><p class="desc">Chicken, Tomato, Pesto in a Creamy<br>White Sauce</p></li>
    <li class="item"><div class="row">Greek Chicken<span class="dots"></span><span class="price">$16.00</span></div><p class="desc">Chicken, Tomato, Fetta, Olives in a Red<br>Pasta Sauce</p></li>
    <li class="item"><div class="row">Garlic Prawn<span class="dots"></span><span class="price">$18.00</span></div><p class="desc">Prawn, Garlic, Onion, Lemon in a<br>Creamy White Sauce</p></li>
    <li class="item"><div class="row">Puttanesca<span class="dots"></span><span class="price">$18.00</span></div><p class="desc">Anchovies, Olives, Capers in a Red<br>Pasta Sauce</p></li>
    <li class="item"><div class="row">Marinara<span class="dots"></span><span class="price">$18.00</span></div><p class="desc">Seafood mix in a Red Pasta Sauce</p></li>
  </ul>

  <header class="section-bar" style="left:892px;top:518px;width:308px;padding-left:48px"><h2>Garlic Sub</h2></header>
  <ul class="list subs" style="left:907px;top:568px;width:275px">
    <li class="item"><div class="row">Pulled Beef</div><p class="desc">Cheese, PulledBeef, Salami, Onion, Mushroom with<br>BBQSauce</p></li>
    <li class="item"><div class="row">Chicken</div><p class="desc">Cheese, SeasonedChicken, Tomato, Onion, Fetta with<br>Sweet Chilli Sauce</p></li>
    <li class="item"><div class="row">Veg</div><p class="desc">Cheese, Tomato, Onion, Mushroom, Capsicum,<br>Pineapple with Tomato Sauce</p></li>
    <li class="item"><div class="row">Meat</div><p class="desc">Cheese, Ham, Pepperoni, Salami,<br>Chorizo with BBQ Sauce</p></li>
    <li class="item"><div class="row">Bacon &amp; Chicken</div><p class="desc">Cheese, SeasonedChicken, Bacon,<br>Mushroom with PeriPeri Sauce</p></li>
  </ul>

  <svg class="seal" viewBox="0 0 100 100" aria-hidden="true">
    <circle cx="50" cy="50" r="45" fill="#2a1517" stroke="#b3272c" stroke-width="8"/>
    <circle cx="50" cy="50" r="38" fill="none" stroke="#6e1a1e" stroke-width="3"/>
  </svg>
  <p class="seal-price">$9.95</p>
</main>
</body>
</html>
```